Labeling for Organic Food

we need a label design for

1. Organic Red Rice
2. Organic wild honey

it is going to be the same design in different dimensions.

1. Organic Red Rice
Dimension 1 28*18.5cm
Dimension 2 13.5*8cm

2. Organic Honey
12*6cm
Updates

Project Deadline Extended Reason: I still haven't found the right design. Added Monday, June 26, 2017

There is an update in the brief about using the Bhutanese color scheme. Please check it out.

Target Market(s)

people with the concern of health and the environment.

Requirements
Must have
• 1. our logo
• 2. All the info
• 3. A natural feel
• 4. I would prefer minimalistic style
• 5. Please include Bhutanese national colours as attached.

```html
<!DOCTYPE html>
<html lang="en">
<head>
<meta charset="utf-8">
<title>Verdanta Organic Red Rice – Label Range</title>
<link rel="stylesheet" href="https://fonts.googleapis.com/css2?family=Courgette&family=Lilita+One&family=Oswald:wght@500;700&family=Roboto+Condensed:wght@400;700&family=Noto+Sans+SC:wght@500&display=swap">
<style>
  :root{
    --stage:#e9ecee;
    --ink-green:#1f7a2a;
    --ink-red:#d3261c;
    --ink-dark:#2a1a10;
    --lime:#7ccc2c;
    --lime-light:#c8ee6a;
    --gold:#f5c31a;
    --badge:#1d5a23;
    --white:#ffffff;
  }
  *{margin:0;padding:0;box-sizing:border-box}
  html,body{width:1200px;height:805px;overflow:hidden;background:var(--stage)}
  .range{position:relative;width:1200px;height:805px}

  .pack{position:absolute;top:110px;width:300px;height:580px;overflow:hidden;background:var(--pattern);box-shadow:0 14px 28px rgba(0,0,0,.18)}
  .pack--violet{left:90px;--cap:#9b4fe0;--pattern:#7d33c6;--pattern-deep:#6a24b0;--band:#7a2fc2}
  .pack--saffron{left:450px;--cap:#4a1d0c;--pattern:#f29a1c;--pattern-deep:#ea8a12;--band:#d8261c}
  .pack--forest{left:810px;--cap:#1d3214;--pattern:#2f4d1f;--pattern-deep:#263f19;--band:#2c4a1c}

  .pack__cap{position:absolute;left:0;top:0;width:100%;height:46px;background:var(--cap)}
  .pack__pattern{position:absolute;left:0;top:46px;width:100%;height:160px;background:linear-gradient(180deg,var(--pattern-deep),var(--pattern))}
  .pack__mark{position:absolute;right:16px;top:54px;width:26px;height:40px;background:var(--gold)}
  .brand{position:absolute;left:0;top:150px;width:100%;text-align:center;font:700 30px/1 "Oswald",sans-serif;color:var(--white);letter-spacing:.5px}

  .pack__art{position:absolute;left:0;top:180px;width:300px;height:300px}
  .veg-mark{position:absolute;left:12px;top:236px;width:12px;height:12px;background:var(--white);border:1px solid #8a8a8a}

  .title{position:absolute;left:0;width:100%;text-align:center}
  .title__organic{top:222px;font:36px/1 "Courgette",cursive;color:var(--ink-green)}
  .title__product{top:258px;font:44px/1 "Lilita One",sans-serif;color:var(--ink-red)}
  .title__cn{top:304px;left:auto;right:62px;width:auto;font:500 14px/1 "Noto Sans SC",sans-serif;color:var(--ink-dark)}

  .origin{position:absolute;left:16px;top:430px;width:52px;height:52px;border-radius:50%;background:var(--badge);border:3px solid var(--gold);color:var(--white);font:400 8px/1.15 "Roboto Condensed",sans-serif;text-align:center;display:flex;flex-direction:column;justify-content:center}
  .origin strong{font-weight:700;font-size:9px}

  .pack__band{position:absolute;left:0;top:440px;width:300px;height:140px}
  .info{position:absolute;top:488px;color:var(--white);font:400 6.6px/1.3 "Roboto Condensed",sans-serif}
  .info--story{left:10px;width:108px}
  .info--distributor{left:124px;width:78px;text-align:center}
  .info--distributor .info__brand{display:block;font:700 11px/1.3 "Oswald",sans-serif;margin:2px 0}
  .info--care{left:210px;width:84px}
  .net-weight{display:inline-block;background:var(--gold);color:var(--ink-dark);font:700 7px/1 "Roboto Condensed",sans-serif;padding:3px 4px;margin-bottom:5px}
</style>
</head>
<body>
<main class="range">

  <section class="pack pack--violet">
    <div class="pack__cap"></div>
    <div class="pack__pattern" role="img" aria-label="Violet damask pattern"></div>
    <div class="pack__mark"></div>
    <svg class="pack__art" viewBox="0 0 300 300">
      <defs>
        <radialGradient id="sun-a" cx="50%" cy="40%" r="70%"><stop offset="0" stop-color="#fff6b0"/><stop offset=".5" stop-color="#f9c02a"/><stop offset="1" stop-color="#e9720f"/></radialGradient>
        <radialGradient id="rice-a" cx="50%" cy="40%" r="60%"><stop offset="0" stop-color="#c2452a"/><stop offset="1" stop-color="#6e1a10"/></radialGradient>
        <linearGradient id="field-a" x1="0" y1="0" x2="0" y2="1"><stop offset="0" stop-color="#9ccf4a"/><stop offset="1" stop-color="#3f7f1e"/></linearGradient>
        <linearGradient id="valley-a" x1="0" y1="0" x2="0" y2="1"><stop offset="0" stop-color="#ffffff"/><stop offset="1" stop-color="#f3d9d4"/></linearGradient>
        <clipPath id="disc-a"><circle cx="150" cy="120" r="92"/></clipPath>
      </defs>
      <rect y="20" width="300" height="280" fill="url(#sun-a)" role="img" aria-label="Orange sunburst"/>
      <path d="M0 44 C90 6 200 44 300 8 L300 34 C200 66 90 30 0 70 Z" fill="var(--lime)"/>
      <path d="M0 62 C90 26 200 60 300 28 L300 36 C200 70 90 36 0 72 Z" fill="var(--lime-light)"/>
      <circle cx="150" cy="120" r="92" fill="#fff"/>
      <rect x="58" y="140" width="184" height="72" fill="url(#valley-a)" clip-path="url(#disc-a)" role="img" aria-label="Sketch of Himalayan terraced valley"/>
      <path d="M0 200 C100 186 200 214 300 196 L300 300 L0 300 Z" fill="url(#field-a)" role="img" aria-label="Green paddy field"/>
      <ellipse cx="150" cy="206" rx="82" ry="32" fill="url(#rice-a)" role="img" aria-label="Pile of red rice grains"/>
    </svg>
    <div class="brand">Verdanta</div>
    <div class="veg-mark"></div>
    <div class="title title__organic">Organic</div>
    <div class="title title__product">Red Rice</div>
    <div class="title title__cn">有机红米</div>
    <svg class="pack__band" viewBox="0 0 300 140">
      <path d="M0 22 C100 0 200 40 300 8 L300 18 C200 50 100 10 0 32 Z" fill="var(--gold)"/>
      <path d="M0 30 C100 8 200 48 300 16 L300 140 L0 140 Z" fill="var(--band)"/>
    </svg>
    <div class="origin"><span>Product of</span><strong>BHUTAN</strong></div>
    <p class="info info--story">This organic red rice is 100% sourced from families farming around the remote unpolluted lands in the Himalayas in Bhutan. Chemical preservatives free, Gluten free, Mineral rich. Organic Red Rice is the healthiest choice for you and your loved ones.</p>
    <p class="info info--distributor">Distributed by<span class="info__brand">Verdanta</span>24 Lotus Park Road,<br>Harbour City 508812</p>
    <div class="info info--care"><span class="net-weight">NET WEIGHT 200gm</span><br>Store in a cool and dry place<br>Ingredients:<br>Organic Bhutanese Red Rice<br>Best before 31.12.19</div>
  </section>

  <section class="pack pack--saffron">
    <div class="pack__cap"></div>
    <div class="pack__pattern" role="img" aria-label="Saffron damask pattern"></div>
    <div class="pack__mark"></div>
    <svg class="pack__art" viewBox="0 0 300 300">
      <defs>
        <radialGradient id="sun-b" cx="50%" cy="40%" r="70%"><stop offset="0" stop-color="#fff6b0"/><stop offset=".5" stop-color="#f9c02a"/><stop offset="1" stop-color="#e9720f"/></radialGradient>
        <radialGradient id="rice-b" cx="50%" cy="40%" r="60%"><stop offset="0" stop-color="#c2452a"/><stop offset="1" stop-color="#6e1a10"/></radialGradient>
        <linearGradient id="field-b" x1="0" y1="0" x2="0" y2="1"><stop offset="0" stop-color="#9ccf4a"/><stop offset="1" stop-color="#3f7f1e"/></linearGradient>
        <linearGradient id="valley-b" x1="0" y1="0" x2="0" y2="1"><stop offset="0" stop-color="#ffffff"/><stop offset="1" stop-color="#f3d9d4"/></linearGradient>
        <clipPath id="disc-b"><circle cx="150" cy="120" r="92"/></clipPath>
      </defs>
      <rect y="20" width="300" height="280" fill="url(#sun-b)" role="img" aria-label="Orange sunburst"/>
      <path d="M0 44 C90 6 200 44 300 8 L300 34 C200 66 90 30 0 70 Z" fill="var(--lime)"/>
      <path d="M0 62 C90 26 200 60 300 28 L300 36 C200 70 90 36 0 72 Z" fill="var(--lime-light)"/>
      <circle cx="150" cy="120" r="92" fill="#fff"/>
      <rect x="58" y="140" width="184" height="72" fill="url(#valley-b)" clip-path="url(#disc-b)" role="img" aria-label="Sketch of Himalayan terraced valley"/>
      <path d="M0 200 C100 186 200 214 300 196 L300 300 L0 300 Z" fill="url(#field-b)" role="img" aria-label="Green paddy field"/>
      <ellipse cx="150" cy="206" rx="82" ry="32" fill="url(#rice-b)" role="img" aria-label="Pile of red rice grains"/>
    </svg>
    <div class="brand">Verdanta</div>
    <div class="veg-mark"></div>
    <div class="title title__organic">Organic</div>
    <div class="title title__product">Red Rice</div>
    <div class="title title__cn">有机红米</div>
    <svg class="pack__band" viewBox="0 0 300 140">
      <path d="M0 22 C100 0 200 40 300 8 L300 18 C200 50 100 10 0 32 Z" fill="var(--gold)"/>
      <path d="M0 30 C100 8 200 48 300 16 L300 140 L0 140 Z" fill="var(--band)"/>
    </svg>
    <div class="origin"><span>Product of</span><strong>BHUTAN</strong></div>
    <p class="info info--story">This organic red rice is 100% sourced from families farming around the remote unpolluted lands in the Himalayas in Bhutan. Chemical preservatives free, Gluten free, Mineral rich. Organic Red Rice is the healthiest choice for you and your loved ones.</p>
    <p class="info info--distributor">Distributed by<span class="info__brand">Verdanta</span>24 Lotus Park Road,<br>Harbour City 508812</p>
    <div class="info info--care"><span class="net-weight">NET WEIGHT 200gm</span><br>Store in a cool and dry place<br>Ingredients:<br>Organic Bhutanese Red Rice<br>Best before 31.12.19</div>
  </section>

  <section class="pack pack--forest">
    <div class="pack__cap"></div>
    <div class="pack__pattern" role="img" aria-label="Forest green damask pattern"></div>
    <div class="pack__mark"></div>
    <svg class="pack__art" viewBox="0 0 300 300">
      <defs>
        <radialGradient id="sun-c" cx="50%" cy="40%" r="70%"><stop offset="0" stop-color="#fff6b0"/><stop offset=".5" stop-color="#f9c02a"/><stop offset="1" stop-color="#e9720f"/></radialGradient>
        <radialGradient id="rice-c" cx="50%" cy="40%" r="60%"><stop offset="0" stop-color="#c2452a"/><stop offset="1" stop-color="#6e1a10"/></radialGradient>
        <linearGradient id="field-c" x1="0" y1="0" x2="0" y2="1"><stop offset="0" stop-color="#9ccf4a"/><stop offset="1" stop-color="#3f7f1e"/></linearGradient>
        <linearGradient id="valley-c" x1="0" y1="0" x2="0" y2="1"><stop offset="0" stop-color="#ffffff"/><stop offset="1" stop-color="#f3d9d4"/></linearGradient>
        <clipPath id="disc-c"><circle cx="150" cy="120" r="92"/></clipPath>
      </defs>
      <rect y="20" width="300" height="280" fill="url(#sun-c)" role="img" aria-label="Orange sunburst"/>
      <path d="M0 44 C90 6 200 44 300 8 L300 34 C200 66 90 30 0 70 Z" fill="var(--lime)"/>
      <path d="M0 62 C90 26 200 60 300 28 L300 36 C200 70 90 36 0 72 Z" fill="var(--lime-light)"/>
      <circle cx="150" cy="120" r="92" fill="#fff"/>
      <rect x="58" y="140" width="184" height="72" fill="url(#valley-c)" clip-path="url(#disc-c)" role="img" aria-label="Sketch of Himalayan terraced valley"/>
      <path d="M0 200 C100 186 200 214 300 196 L300 300 L0 300 Z" fill="url(#field-c)" role="img" aria-label="Green paddy field"/>
      <ellipse cx="150" cy="206" rx="82" ry="32" fill="url(#rice-c)" role="img" aria-label="Pile of red rice grains"/>
    </svg>
    <div class="brand">Verdanta</div>
    <div class="veg-mark"></div>
    <div class="title title__organic">Organic</div>
    <div class="title title__product">Red Rice</div>
    <div class="title title__cn">有机红米</div>
    <svg class="pack__band" viewBox="0 0 300 140">
      <path d="M0 22 C100 0 200 40 300 8 L300 18 C200 50 100 10 0 32 Z" fill="var(--gold)"/>
      <path d="M0 30 C100 8 200 48 300 16 L300 140 L0 140 Z" fill="var(--band)"/>
    </svg>
    <div class="origin"><span>Product of</span><strong>BHUTAN</strong></div>
    <p class="info info--story">This organic red rice is 100% sourced from families farming around the remote unpolluted lands in the Himalayas in Bhutan. Chemical preservatives free, Gluten free, Mineral rich. Organic Red Rice is the healthiest choice for you and your loved ones.</p>
    <p class="info info--distributor">Distributed by<span class="info__brand">Verdanta</span>24 Lotus Park Road,<br>Harbour City 508812</p>
    <div class="info info--care"><span class="net-weight">NET WEIGHT 500gm</span><br>Store in a cool and dry place<br>Ingredients:<br>Organic Bhutanese Red Rice<br>Best before 31.12.19</div>
  </section>

</main>
</body>
</html>
```